Stationary for IT communtications company
We send SMS and email messages to pet owners from veterinary practices
Stationary for IT communtications company - Information Technology
Creative Brief
Modern
Dominic Pelling MRCVS
Mr
Oakmere Stanhurst Lode Norwich NR14 2QJ
dominic@quietnudge.co.uk
www.quietnudge.co.uk
Quiet Nudge Logo

```html
<!DOCTYPE html>
<html lang="en">
<head>
<meta charset="utf-8">
<title>Quiet Nudge – Business Card</title>
<link rel="stylesheet" href="https://fonts.googleapis.com/css2?family=Open+Sans:wght@400;600;700&display=swap">
<style>
  :root {
    --backdrop: #e6e4e1;
    --card-white: #ffffff;
    --card-black: #1b1b1b;
    --brand-green: #7cc242;
    --deep-green: #2f8a1f;
    --ink: #4a4a4a;
    --ink-soft: #6b6b6b;
    --rule: #c9c9c9;
  }
  * { margin: 0; padding: 0; box-sizing: border-box; }
  html, body {
    width: 1200px; height: 1033px; overflow: hidden;
    background: var(--backdrop);
    font-family: "Open Sans", Arial, sans-serif;
  }
  .stage { position: relative; width: 1200px; height: 1033px; }

  .card {
    position: absolute;
    border-radius: 26px;
    overflow: hidden;
    box-shadow: 0 10px 26px rgba(0,0,0,0.28);
  }

  /* Front */
  .card-front {
    left: 140px; top: 60px; width: 700px; height: 470px;
    background: var(--card-white);
  }
  .front-brand {
    position: absolute; left: 175px; top: 62px;
    display: flex; align-items: center; gap: 22px;
  }
  .brand-square { width: 64px; height: 64px; background: var(--brand-green); }
  .brand-name {
    font-size: 58px; font-weight: 700; color: var(--ink);
    letter-spacing: 1px; line-height: 1;
  }
  .front-address {
    position: absolute; left: 150px; top: 245px; width: 220px;
    text-align: right; font-size: 17px; line-height: 26px; color: var(--ink-soft);
  }
  .front-divider {
    position: absolute; left: 392px; top: 245px; width: 1px; height: 80px;
    background: var(--rule);
  }
  .front-contacts {
    position: absolute; left: 406px; top: 243px; list-style: none;
    font-size: 17px; line-height: 27px; color: var(--ink-soft);
  }
  .front-contacts li { display: flex; align-items: center; gap: 8px; }
  .front-contacts svg { width: 14px; height: 14px; flex: none; }
  .front-swoosh { position: absolute; left: 0; bottom: 0; width: 700px; height: 150px; }
  .front-name {
    position: absolute; left: 28px; bottom: 28px;
    font-size: 24px; font-weight: 700; color: #fff;
  }

  /* Back */
  .card-back {
    left: 560px; top: 555px; width: 580px; height: 410px;
    background: var(--card-black);
  }
  .back-brand {
    position: absolute; left: 0; right: 0; top: 145px;
    display: flex; justify-content: center; align-items: center; gap: 18px;
  }
  .back-brand .brand-square { width: 50px; height: 50px; }
  .back-brand .brand-name { color: #fff; font-size: 46px; }
  .back-url {
    position: absolute; left: 0; right: 0; bottom: 55px; text-align: center;
    font-size: 22px; color: #fff; font-weight: 400;
  }
  .back-url .url-domain { color: var(--brand-green); font-weight: 700; }
</style>
</head>
<body>
<main class="stage">

  <section class="card card-front" aria-label="Business card front">
    <div class="front-brand">
      <span class="brand-square" aria-hidden="true"></span>
      <span class="brand-name">Quiet Nudge</span>
    </div>

    <p class="front-address">Oakmere Stanhurst<br>Lode, Norwich NR14 2QJ</p>
    <span class="front-divider" aria-hidden="true"></span>
    <ul class="front-contacts">
      <li>
        <svg viewBox="0 0 14 14" aria-hidden="true"><rect x="3.5" y="1" width="7" height="12" rx="1.5" fill="var(--deep-green)"/><rect x="5" y="3" width="4" height="6" fill="#fff"/></svg>
        0-781-642-7190
      </li>
      <li>
        <svg viewBox="0 0 14 14" aria-hidden="true"><rect x="1" y="3" width="12" height="8" rx="1" fill="var(--deep-green)"/><path d="M1.5 3.5 L7 8 L12.5 3.5" stroke="#fff" stroke-width="1.2" fill="none"/></svg>
        dominic@quietnudge.co.uk
      </li>
      <li>
        <svg viewBox="0 0 14 14" aria-hidden="true"><circle cx="7" cy="7" r="6" fill="var(--deep-green)"/><path d="M1 7 H13 M7 1 C4 4 4 10 7 13 M7 1 C10 4 10 10 7 13" stroke="#fff" stroke-width="0.9" fill="none"/></svg>
        www.quietnudge.co.uk
      </li>
    </ul>

    <svg class="front-swoosh" viewBox="0 0 700 150" preserveAspectRatio="none" aria-hidden="true">
      <defs>
        <linearGradient id="swoosh-green" x1="0" y1="0" x2="1" y2="0">
          <stop offset="0" stop-color="#2a7d1b"/>
          <stop offset="0.6" stop-color="#4ea62c"/>
          <stop offset="1" stop-color="#7cc242"/>
        </linearGradient>
        <linearGradient id="swoosh-grey" x1="0" y1="0" x2="1" y2="0">
          <stop offset="0" stop-color="#d8d8d8"/>
          <stop offset="1" stop-color="#9a9a9a"/>
        </linearGradient>
      </defs>
      <path d="M0 55 C180 110 420 10 700 30 L700 150 L0 150 Z" fill="url(#swoosh-grey)"/>
      <path d="M0 78 C200 118 430 38 700 52 L700 150 L0 150 Z" fill="#2b2b2b"/>
      <path d="M0 92 C210 126 440 58 700 72 L700 150 L0 150 Z" fill="url(#swoosh-green)"/>
    </svg>
    <p class="front-name">Mr. Dominic Pelling MRCVS</p>
  </section>

  <section class="card card-back" aria-label="Business card back">
    <div class="back-brand">
      <span class="brand-square" aria-hidden="true"></span>
      <span class="brand-name">Quiet Nudge</span>
    </div>
    <p class="back-url">www.<span class="url-domain">quietnudge</span>.co.uk</p>
  </section>

</main>
</body>
</html>
```